Zielgruppe
Ich betreibe eine mobile Hundeschule / Hundetraining. Meine Zielgruppe sind Hundehalter:innen, junge Menschen und jung Gebliebene.
Aufgabenstellung
Das Design soll in erster Linie modern sein, aber auch kompetent und sympathisch wirken. Texte würde ich gerne in Absprache mit dem Designer erstellen.
Ich wünsche mir einen Faltflyer in Standardgröße (ich glaube das heißt DIN lang, 2 mal gefaltet (Wickelfalz), 99x210mm.
IM AMHANG SIND BILDER DER NEUEN HOMEPAGE. DIESE IST NCOH NICHT ONLINE. DAS DESIGN SOLL SICH GERNE AN DEN BILDERN DER HOMEPAGE ORIENTIEREN.

```html
<!DOCTYPE html>
<html lang="de">
<head>
<meta charset="utf-8">
<title>Hundeakademie Wiesental – Faltflyer</title>
<link rel="stylesheet" href="https://fonts.googleapis.com/css2?family=Zilla+Slab:ital,wght@0,300;0,400;0,600;0,700;1,300;1,400&display=swap">
<style>
  :root{
    --orange:#d89a2e;
    --orange-light:#e2a83f;
    --orange-soft:#f3d9a4;
    --brown:#6b3e2a;
    --brown-text:#7a5040;
    --white:#ffffff;
    --paper:#f7f6f4;
    --stage:#e8e8e8;
    --font:"Zilla Slab", Georgia, serif;
  }
  *{box-sizing:border-box;margin:0;padding:0}
  html,body{width:1200px;height:900px;overflow:hidden}
  body{background:var(--stage);font-family:var(--font);color:var(--brown-text);position:relative}

  .spread{position:absolute;left:296px;width:609px;height:430px;display:flex;box-shadow:0 6px 18px rgba(0,0,0,.15)}
  .spread--outside{top:12px}
  .spread--inside{top:458px}
  .panel{position:relative;width:203px;height:430px;overflow:hidden}

  /* Outside: about panel */
  .about{background:var(--white)}
  .about__photo{position:absolute;left:0;top:0;width:203px;height:152px;border:3px solid var(--orange);
    background:linear-gradient(180deg,#6d7a4e 0%,#a58b5a 45%,#8a6b45 100%)}
  .about__content{position:absolute;left:8px;right:8px;top:158px}
  .section-title{font-weight:700;font-size:9.5px;color:var(--brown);text-align:center;margin:6px 0 3px}
  .paw-list{list-style:none}
  .paw-list li{position:relative;padding-left:14px;font-size:7.8px;line-height:9px;font-weight:300;color:var(--brown-text)}
  .paw-list li svg{position:absolute;left:1px;top:1px;width:7px;height:7px;color:var(--orange)}
  .contact-band{position:absolute;left:0;bottom:0;width:203px;height:40px;background:var(--orange);color:var(--white);
    text-align:center;font-weight:700;font-size:8.6px;line-height:15px;padding-top:5px}

  /* Outside: cover photo across two panels */
  .cover{position:relative;width:406px;height:430px;overflow:hidden}
  .cover__photo{position:absolute;inset:0;
    background:linear-gradient(180deg,#ffffff 0%,#e9ebe8 12%,#9aa296 26%,#74755a 38%,#8c7550 55%,#a98a5c 75%,#8a6a44 100%)}
  .cover__fade{position:absolute;left:203px;top:0;width:203px;height:120px;background:linear-gradient(180deg,#cfcfcf 0%,rgba(207,207,207,.6) 55%,rgba(207,207,207,0) 100%)}
  .cover__quote{position:absolute;left:0;top:92px;width:203px;text-align:center;color:var(--white);font-weight:300;font-size:11.5px;line-height:14.5px}
  .cover__quote cite{display:block;font-style:italic}
  .cover__band{position:absolute;left:0;bottom:0;width:203px;height:40px;background:rgba(216,154,46,.85)}
  .brand{position:absolute;left:203px;top:18px;width:203px;display:flex;align-items:center;justify-content:center;gap:6px}
  .brand__dot{width:20px;height:20px;border-radius:50%;background:var(--orange)}
  .brand__name{font-weight:700;font-size:10px;line-height:11px;color:var(--brown);text-transform:uppercase;letter-spacing:.3px}

  /* Inside: offers */
  .offers{background:var(--orange)}
  .offers-photos{background:var(--orange-light)}
  .offer{position:absolute;left:22px;width:181px;height:124px;border:1.5px solid var(--orange-soft);border-right:none;
    text-align:center;color:var(--orange-soft);padding-top:18px}
  .offer--1{top:20px}.offer--2{top:152px}.offer--3{top:284px}
  .offer__title{font-weight:700;font-size:10px;color:#f8e6c2}
  .offer__sub{font-weight:300;font-size:7.5px;margin-top:3px}
  .offer__rule{width:40px;height:1px;background:var(--orange-soft);margin:9px auto}
  .offer__text{font-weight:300;font-size:7.5px;line-height:8.5px}
  .offer__note{font-style:italic;font-weight:300;font-size:7px;line-height:8px;margin-top:9px;color:#eec98a}
  .hours{position:absolute;left:28px;bottom:12px;font-style:italic;font-weight:300;font-size:7px;color:#eec98a}
  .offer-photo{position:absolute;left:6px;width:184px;height:118px;border:2px solid var(--white)}
  .offer-photo--1{top:23px;background:linear-gradient(160deg,#7a4a30 0%,#c58a4e 50%,#5a3a26 100%)}
  .offer-photo--2{top:155px;background:linear-gradient(170deg,#4b6a3d 0%,#8d8470 45%,#8a5a44 100%)}
  .offer-photo--3{top:287px;background:linear-gradient(160deg,#2f3a2c 0%,#5a5a44 45%,#9a5a30 100%)}

  /* Inside: values */
  .values{background:var(--paper)}
  .values__frame{position:absolute;inset:4px 6px;border:1px solid var(--brown);outline:1px solid rgba(107,62,42,.35);outline-offset:-4px}
  .value{position:absolute;left:14px;right:14px;text-align:center}
  .value--1{top:34px}.value--2{top:160px}.value--3{top:286px}
  .value svg{display:block;margin:0 auto;height:36px;width:36px}
  .value__title{font-weight:700;font-size:9.5px;color:var(--brown);margin:12px 0 8px}
  .value__text{font-weight:300;font-size:7.8px;line-height:9.2px;color:var(--brown-text)}
</style>
</head>
<body>

<svg width="0" height="0" style="position:absolute">
  <defs>
    <symbol id="paw" viewBox="0 0 24 24">
      <ellipse cx="12" cy="16" rx="6" ry="5" fill="currentColor"/>
      <ellipse cx="5" cy="9" rx="2.3" ry="3" fill="currentColor"/>
      <ellipse cx="9.5" cy="5" rx="2.3" ry="3" fill="currentColor"/>
      <ellipse cx="14.5" cy="5" rx="2.3" ry="3" fill="currentColor"/>
      <ellipse cx="19" cy="9" rx="2.3" ry="3" fill="currentColor"/>
    </symbol>
  </defs>
</svg>

<section class="spread spread--outside">
  <div class="panel about">
    <div class="about__photo" role="img" aria-label="Foto: Hundetrainerin kniet mit ihrem Hund im hohen Gras"></div>
    <div class="about__content">
      <h3 class="section-title">Trainingsphilosophie</h3>
      <ul class="paw-list">
        <li><svg><use href="#paw"/></svg>positive Verstärkung anwenden</li>
        <li><svg><use href="#paw"/></svg>keine Strafreize wie einschüchtern oder Schmerzen zufügen</li>
        <li><svg><use href="#paw"/></svg>individuelle Bedürfnisse der Hunde berücksichtigen</li>
      </ul>
      <h3 class="section-title">Mein Training</h3>
      <ul class="paw-list">
        <li><svg><use href="#paw"/></svg>Erkenntnisse der modernen Verhaltens­forschung</li>
        <li><svg><use href="#paw"/></svg>regelmäßige Teilnahme an Fortbildungen im In- und Ausland</li>
      </ul>
      <h3 class="section-title">Meine Ausbildung</h3>
      <ul class="paw-list">
        <li><svg><use href="#paw"/></svg>zweijährige Ausbildung zur Hundetrainerin und Verhaltensberaterin bei Marlene Osterkamp-Wiese (Canivera®)</li>
        <li><svg><use href="#paw"/></svg>durch das Veterinäramt des Kreises Halbergen geprüft und es wurde</li>
        <li><svg><use href="#paw"/></svg>Erlaubnis nach § 11 des TierSchG erteilt</li>
      </ul>
    </div>
    <div class="contact-band">
      <div>info@hundeakademie-wiesental.de</div>
      <div>0170 / 238 40 61 9</div>
    </div>
  </div>

  <div class="cover">
    <div class="cover__photo" role="img" aria-label="Foto: brauner Hund sitzt in einer herbstlichen Heidelandschaft"></div>
    <div class="cover__fade"></div>
    <blockquote class="cover__quote">
      "Egal wie wenig<br>Geld und Besitz du hast,<br>einen Hund zu haben,<br>macht dich reich"
      <cite>Jonas Feldmann</cite>
    </blockquote>
    <div class="cover__band"></div>
    <div class="brand">
      <span class="brand__dot"></span>
      <span class="brand__name">Hundeakademie<br>Wiesental</span>
    </div>
  </div>
</section>

<section class="spread spread--inside">
  <div class="panel offers">
    <div class="offer offer--1">
      <div class="offer__title">Einzeltraining</div>
      <div class="offer__sub">1:1 Coaching</div>
      <div class="offer__rule"></div>
      <div class="offer__text">Optimal bei Problemen<br>oder exklusives Training</div>
      <div class="offer__note">Für Welpen, Junghunde<br>und erwachsene Hunde</div>
    </div>
    <div class="offer offer--2">
      <div class="offer__title">Gruppentraining</div>
      <div class="offer__sub">Spaß in der Gruppe</div>
      <div class="offer__rule"></div>
      <div class="offer__text">Optimal für Alltagstraining<br>und Beschäftigung</div>
      <div class="offer__note">Für Welpen, Junghunde<br>und erwachsene Hunde</div>
    </div>
    <div class="offer offer--3">
      <div class="offer__title">Workshops</div>
      <div class="offer__sub">Kompaktes Training</div>
      <div class="offer__rule"></div>
      <div class="offer__text">Optimal für effektives Training<br>in kurzer Zeit</div>
      <div class="offer__note">Für Hunde ab 10 Monate</div>
    </div>
    <div class="hours">Trainingszeiten täglich 9-19 Uhr</div>
  </div>

  <div class="panel offers-photos">
    <div class="offer-photo offer-photo--1" role="img" aria-label="Foto: Welpe läuft im Abendlicht über einen Weg"></div>
    <div class="offer-photo offer-photo--2" role="img" aria-label="Foto: mehrere Hunde an der Leine in einem Park"></div>
    <div class="offer-photo offer-photo--3" role="img" aria-label="Foto: Frau mit Hund im Wald"></div>
  </div>

  <div class="panel values">
    <div class="values__frame"></div>
    <div class="value value--1">
      <svg viewBox="0 0 24 24" style="color:var(--orange)"><use href="#paw"/></svg>
      <div class="value__title">Hundgerecht</div>
      <p class="value__text">Mit modernen Trainingsmethoden brauchst du keine Gewalt. Dein Hund lernt mit Spaß und eure Bindung wird gestärkt.</p>
    </div>
    <div class="value value--2">
      <svg viewBox="0 0 36 36"><path d="M18 8 L34 15 L18 22 L2 15 Z" fill="var(--orange)"/><path d="M9 19 V26 C13 30 23 30 27 26 V19 L18 23 Z" fill="var(--orange)"/><path d="M31 16 V24" stroke="var(--orange)" stroke-width="1.5"/></svg>
      <div class="value__title">Fundiert</div>
      <p class="value__text">Unsere Trainingsmethoden basieren auf den neuesten Erkenntnissen aus der Verhaltensfor­schung und aktuellen Trainingstechniken.</p>
    </div>
    <div class="value value--3">
      <svg viewBox="0 0 36 36"><rect x="7" y="5" width="22" height="29" rx="1.5" fill="var(--orange)"/><rect x="13" y="3" width="10" height="5" rx="1" fill="var(--orange)" stroke="var(--paper)" stroke-width="1"/><g stroke="var(--paper)" stroke-width="1.5"><path d="M11 14h2M15 14h10M11 19h2M15 19h10M11 24h2M15 24h10"/></g></svg>
      <div class="value__title">Erfolgreich</div>
      <p class="value__text">Durch fundiertes Hintergrundwissen und Ver­wendung verschiedener Trainingstechniken, erreichst du dauerhafte Trainingserfolge.</p>
    </div>
  </div>
</section>

</body>
</html>
```